Cloud Hosted Phone System for small and medium sized businesses

I want to design a one A4 page size single or double sided brochure to offer cloud hosted VoIP Phone system and a complete collaboration system. We have partnered with a VoIP Phone system company and want to sell their services but we don't want their name to be shown on the brochure because customers might call them directly. The company name is Corvane (www.corvane-example.com) and our company name is KESTRAL Tech Solutions. I have also uploaded my compnay's logo that you should show on the brochure. For more details about the product, you can visit their website as mentioned above.

Reason: Not getting a design to my liking.

Target Market(s)

Small and medium sized business including law firms, marketing and advertising agencies, real-estate firms and others.

Industry/Entity Type

Voip

Colors

Designer to choose colors to be used in the design.

Requirements
Must have
• My company's Logo (KESTRAL Tech Solutions). Price list, services and some images to show the benefits and services of the cloud based and advanced VoIP phone system. I want the brochure to look very professional and attractive.
• Contact US: Our company's name, Logo, web address, phone (555-371-9046) and email (info@kestraltechsolutions-example.com)
Nice to have
• It is a Canadian based company and all of our servers and customers’ data reside in Canada.

```html
<!DOCTYPE html>
<html lang="en">
<head>
<meta charset="utf-8">
<title>KESTRAL Tech Solutions – Cloud-Based Phone System</title>
<link href="https://fonts.googleapis.com/css2?family=Open+Sans:wght@400;600;700;800&display=swap" rel="stylesheet">
<style>
  :root {
    --blue: #1b5ea8;
    --blue-deep: #0f47a6;
    --blue-band: #1a63c4;
    --ink: #1e2125;
    --text: #2c2f33;
    --sky-top: #ffffff;
    --sky-bottom: #d7f0fb;
    --bar: #0b0b0b;
    --white: #ffffff;
    --cable: #e7c21c;
    --rack: #1c1f24;
  }
  * { margin: 0; padding: 0; box-sizing: border-box; }
  html, body { width: 932px; height: 1200px; overflow: hidden; background: #ffffff; }
  body { font-family: "Open Sans", Arial, sans-serif; color: var(--text); }

  .brochure {
    position: relative; width: 932px; height: 1200px; overflow: hidden;
    background: linear-gradient(180deg, var(--sky-top) 0%, var(--sky-top) 36%, #eef9fd 55%, var(--sky-bottom) 85%);
  }

  .hero { position: absolute; left: 0; top: 0; width: 932px; height: 370px; }

  .brand { position: absolute; left: 58px; top: 342px; display: flex; align-items: center; gap: 14px; }
  .brand-dot { width: 62px; height: 62px; border-radius: 50%; background: var(--blue); }
  .brand-name { font-size: 40px; font-weight: 600; color: var(--ink); letter-spacing: 0.5px; line-height: 1; }

  .intro { position: absolute; left: 58px; top: 470px; width: 830px; }
  .headline { font-size: 26px; font-weight: 800; color: var(--blue); letter-spacing: 0.3px; line-height: 1.2; }
  .intro p { font-size: 15px; line-height: 19.5px; margin-top: 4px; }
  .intro p + p { margin-top: 11px; }

  .benefits { position: absolute; left: 58px; top: 640px; width: 830px; }
  .benefits-title { font-size: 26px; font-weight: 800; color: var(--ink); line-height: 1.2; }
  .benefit { position: relative; padding-left: 34px; margin-top: 12px; }
  .benefit::before {
    content: ""; position: absolute; left: 2px; top: 8px; width: 10px; height: 10px;
    border-radius: 50%; background: var(--blue);
  }
  .benefit h3 { font-size: 21px; font-weight: 600; color: var(--blue); line-height: 1.2; }
  .benefit p { font-size: 15px; line-height: 19.5px; margin-top: 3px; }
  .benefit + .benefit { margin-top: 10px; }

  .services {
    position: absolute; left: 0; top: 1021px; width: 932px; height: 140px;
    background: linear-gradient(90deg, #1e6cc8 0%, var(--blue-band) 50%, var(--blue-deep) 100%);
    color: var(--white);
  }
  .services-title { text-align: center; font-size: 26px; font-weight: 600; padding-top: 7px; line-height: 34px; }
  .services-rule { position: absolute; left: 160px; top: 44px; width: 610px; height: 1px; background: rgba(255,255,255,0.7); }
  .services-rule::after { content: ""; position: absolute; left: 200px; top: -1px; width: 220px; height: 3px; background: var(--white); }
  .service-list { position: absolute; left: 0; top: 52px; width: 932px; height: 88px; display: flex; list-style: none; }
  .service { text-align: center; display: flex; flex-direction: column; align-items: center; }
  .service + .service { border-left: 1px solid rgba(255,255,255,0.75); }
  .service svg { width: 56px; height: 58px; margin-top: 4px; }
  .service span { font-size: 15px; margin-top: 6px; }
  .s1 { width: 306px; }
  .s2 { width: 230px; }
  .s3 { width: 160px; }
  .s4 { width: 236px; align-items: flex-start; padding-left: 22px; }
  .s4 svg { margin-left: 14px; }
  .s1 { padding-left: 110px; }

  .contact-bar {
    position: absolute; left: 0; top: 1161px; width: 932px; height: 39px; background: var(--bar);
    color: var(--white); display: flex; align-items: center; justify-content: center; font-size: 16px; gap: 12px;
  }
  .contact-bar .sep { width: 1px; height: 20px; background: var(--white); }
  .contact-bar b { font-weight: 700; }
  .contact-bar .item { display: flex; align-items: center; gap: 8px; }
  .contact-bar svg { width: 16px; height: 16px; }
</style>
</head>
<body>
<main class="brochure">

  <svg class="hero" viewBox="0 0 932 370" role="img" aria-label="Photo of yellow network patch cables plugged into a server switch, framed in a cloud shape">
    <defs>
      <linearGradient id="cables" x1="0" y1="0" x2="1" y2="1">
        <stop offset="0" stop-color="#d8b21a"/>
        <stop offset="0.45" stop-color="#e7c21c"/>
        <stop offset="0.7" stop-color="#8a8f96"/>
        <stop offset="1" stop-color="#1c1f24"/>
      </linearGradient>
    </defs>
    <path d="M24 0 H932 V94 C920 140 880 160 850 170 C820 230 770 270 720 275 C700 330 630 370 560 355 C500 370 440 345 420 300 C370 320 310 300 290 260 C240 270 200 240 190 215 C120 225 60 190 40 140 C20 110 18 60 24 0 Z"
          fill="url(#cables)" stroke="#ffffff" stroke-width="8"/>
  </svg>

  <div class="brand">
    <div class="brand-dot"></div>
    <div class="brand-name">KESTRAL Tech Solutions</div>
  </div>

  <section class="intro">
    <h1 class="headline">A CLOUD-BASED PHONE SYSTEM FOR BUSINESSES</h1>
    <p>We can help you grow your business by modernizing your company's phone system and making it easy to use, manage, and track directly from the cloud</p>
    <p>Our cloud business phone system adapts to your economic challenges and brings flexibility and adaptability to your business communications whilst considerably reducing costs compared to traditional phone systems. We take great pride in continually improving our platform as well as developing new features and services that in turn increase our customers' productivity.</p>
  </section>

  <section class="benefits">
    <h2 class="benefits-title">BENEFITS OF CLOUD-BASED PHONE SYSTEM</h2>
    <div class="benefit">
      <h3>Become Mobile</h3>
      <p>From our cloud-based telephony and its unified communications system emerges the concept of mobility. Make calls using your office phone, computer, or mobile phone, and chat with your colleagues and customers from numerous locations. Enjoy centralized communications and simplified management.</p>
    </div>
    <div class="benefit">
      <h3>Stay Abreast</h3>
      <p>Enjoy leading-edge telecommunications technology and its host of features that adapt to your needs, whatever the size of your business. These features are constantly upscaled and automatically updated. You will thus never have to operate an obsolete system.</p>
    </div>
    <div class="benefit">
      <h3>Avoid Inconveniences</h3>
      <p>We take charge of the structure of your business phone system and remove the PBX (Private Branch Exchange) system to host it in its cloud database, thus saving you space, time, and costs. You are cleared of wire clutter and your business communications are streamlined, allowing you to work freely and efficiently. Also, this service includes an excellent recovery and business continuity plan that prevents unforeseen events, such as claims or system failures, from leading to data loss or suspension of business activities.</p>
    </div>
  </section>

  <section class="services">
    <h2 class="services-title">A Cloud-based Phone System For Businesses</h2>
    <div class="services-rule"></div>
    <ul class="service-list">
      <li class="service s1">
        <svg viewBox="0 0 56 58" fill="#ffffff" aria-hidden="true">
          <rect x="6" y="14" width="10" height="40" rx="3"/>
          <rect x="19" y="8" width="30" height="46" rx="3"/>
          <rect x="23" y="12" width="22" height="10" fill="#1a63c4"/>
          <g fill="#1a63c4"><rect x="23" y="26" width="5" height="5"/><rect x="31" y="26" width="5" height="5"/><rect x="39" y="26" width="5" height="5"/><rect x="23" y="34" width="5" height="5"/><rect x="31" y="34" width="5" height="5"/><rect x="39" y="34" width="5" height="5"/><rect x="23" y="42" width="5" height="5"/><rect x="31" y="42" width="5" height="5"/><rect x="39" y="42" width="5" height="5"/></g>
        </svg>
        <span>Cloud Phone System</span>
      </li>
      <li class="service s2">
        <svg viewBox="0 0 56 58" fill="#ffffff" aria-hidden="true">
          <circle cx="12" cy="12" r="6"/><circle cx="28" cy="9" r="6"/><circle cx="44" cy="12" r="6"/>
          <rect x="4" y="21" width="16" height="18" rx="4"/><rect x="20" y="18" width="16" height="20" rx="4"/><rect x="36" y="21" width="16" height="18" rx="4"/>
          <rect x="8" y="38" width="40" height="5"/><rect x="12" y="43" width="5" height="12"/><rect x="39" y="43" width="5" height="12"/>
        </svg>
        <span>Unified Communications</span>
      </li>
      <li class="service s3">
        <svg viewBox="0 0 56 58" fill="none" stroke="#ffffff" stroke-width="4" aria-hidden="true">
          <path d="M10 32 V26 A18 18 0 0 1 46 26 V32"/>
          <rect x="5" y="28" width="9" height="16" rx="3" fill="#ffffff"/>
          <rect x="42" y="28" width="9" height="16" rx="3" fill="#ffffff"/>
          <path d="M46 44 C46 52 38 54 30 54"/>
        </svg>
        <span>Contact Center</span>
      </li>
      <li class="service s4">
        <svg viewBox="0 0 56 58" fill="#ffffff" aria-hidden="true">
          <circle cx="18" cy="10" r="7"/>
          <path d="M10 20 H24 L28 34 H40 V40 H22 L10 40 Z"/>
          <rect x="14" y="40" width="6" height="16"/>
          <rect x="26" y="40" width="5" height="16"/>
          <rect x="30" y="26" width="24" height="4"/>
          <rect x="48" y="30" width="4" height="26"/>
          <rect x="38" y="12" width="3" height="14" transform="rotate(20 40 19)"/>
        </svg>
        <span>Meet Studio</span>
      </li>
    </ul>
  </section>

  <footer class="contact-bar">
    <span>Call Us: <b>555-371-9046</b></span>
    <span class="sep"></span>
    <span class="item">
      <svg viewBox="0 0 16 16" fill="none" stroke="#ffffff" stroke-width="1.3" aria-hidden="true"><circle cx="8" cy="8" r="6.5"/><ellipse cx="8" cy="8" rx="3" ry="6.5"/><path d="M1.5 8 H14.5"/></svg>
      www.<b>kestraltechsolutions-example</b>.com
    </span>
    <span class="sep"></span>
    <span class="item">
      <svg viewBox="0 0 16 16" fill="none" stroke="#ffffff" stroke-width="1.3" aria-hidden="true"><circle cx="8" cy="8" r="6.5"/><path d="M5.5 4.5 L7 6.5 L6 7.5 C6.5 8.7 7.3 9.5 8.5 10 L9.5 9 L11.5 10.5 L10.5 11.8 C7.5 11.5 4.5 8.5 4.2 5.5 Z" fill="#ffffff" stroke="none"/></svg>
      info@<b>kestraltechsolutions-example</b>.com
    </span>
  </footer>

</main>
</body>
</html>
```